Vexel Business Cards

We need a new look business cvard to refelect our new look website www.vexel-example.com.au
We’re Vexel, a team of town planning and traffic and transport engineering specialists located in Melbourne.

Vexel is a company that is structured, articulate, dynamic, progressive, accurate and adaptable.
Our key messages are:
1. We make your life easier by doing what we do best
2. We tell you what you need to know not what you want to hear
3. Polished and professional but not afraid to show some personality

we would like a bold new look that is polished and professional but not afraid to show a bit of personality

Target Market(s)

Vexel’s diverse client base consists of architecture practices, builders, developers, local government and the legal fraternity.

Industry/Entity Type

Town

Requirements
Must have
• must use our logo and have the following information

Joel Harcastle
Director

Vexel Consultants Pty Ltd
Fernhollow first floor
Tamber Street
Elmbrook NVA 3999 Australia
+61 03 9555 0187
mail@vexel-example.com.au
www.vexel-example.com.au
Nice to have
• We would like to see the logo used or the colours of the logo used.

```html
<!DOCTYPE html>
<html lang="en">
<head>
<meta charset="utf-8">
<title>Vexel Business Cards</title>
<link rel="stylesheet" href="https://fonts.googleapis.com/css2?family=Roboto:wght@300;500&display=swap">
<style>
  :root {
    --backdrop: #d9d6d1;
    --frame: #e8e8e8;
    --paper: #f6f6f6;
    --green: #5bb26d;
    --blue: #4d96c8;
    --slate: #6c7884;
    --white: #ffffff;
    --shadow: rgba(0, 0, 0, 0.22);
  }
  * { box-sizing: border-box; margin: 0; padding: 0; }
  html, body { width: 1200px; height: 900px; overflow: hidden; }
  body {
    background: var(--backdrop);
    font-family: "Roboto", Helvetica, Arial, sans-serif;
    font-weight: 300;
    display: flex;
    align-items: center;
    justify-content: center;
    gap: 90px;
  }
  .card {
    width: 380px;
    height: 640px;
    background: var(--frame);
    padding: 18px;
    box-shadow: 0 14px 30px var(--shadow);
    display: flex;
    flex-direction: column;
    gap: 14px;
  }
  /* Front */
  .card-front .brand-panel {
    flex: 1;
    background: var(--paper);
    display: flex;
    align-items: center;
    justify-content: center;
    gap: 16px;
  }
  .brand-square {
    width: 54px;
    height: 54px;
    background: var(--green);
  }
  .brand-name {
    font-size: 58px;
    color: var(--slate);
    letter-spacing: 1px;
  }
  .web-band {
    align-self: flex-end;
    width: 78%;
    height: 86px;
    background: var(--green);
    color: var(--white);
    display: flex;
    align-items: center;
    justify-content: center;
    font-size: 16px;
  }
  /* Back */
  .panel {
    color: var(--white);
    display: flex;
    flex-direction: column;
    align-items: center;
    justify-content: center;
    text-align: center;
    gap: 10px;
  }
  .panel-name {
    background: var(--blue);
    height: 152px;
    gap: 2px;
  }
  .holder-name { font-size: 26px; letter-spacing: 0.5px; }
  .holder-role { font-size: 15px; }
  .holder-brand { font-size: 26px; font-weight: 500; margin-top: 6px; }
  .panel-contact {
    background: var(--green);
    flex: 1;
    font-size: 18px;
    line-height: 1.35;
  }
  .panel-contact.address { font-size: 17px; }
  .icon { width: 28px; height: 28px; }
</style>
</head>
<body>

<section class="card card-front" aria-label="Card front">
  <div class="brand-panel">
    <span class="brand-square"></span>
    <span class="brand-name">vexel</span>
  </div>
  <div class="web-band">www.vexel-example.com.au</div>
</section>

<section class="card card-back" aria-label="Card back">
  <div class="panel panel-name">
    <p class="holder-name">JOEL HARCASTLE</p>
    <p class="holder-role">Director</p>
    <p class="holder-brand">vexel</p>
  </div>

  <div class="panel panel-contact">
    <svg class="icon" viewBox="0 0 28 28" aria-hidden="true">
      <circle cx="14" cy="14" r="12.5" fill="none" stroke="#fff" stroke-width="1.5"/>
      <path d="M10 8.5c-1 1-1 3 1 5.5s4.5 4.5 6 4.5c1 0 2-1 2-1l-2-2-1.5 1c-1 0-3.5-2.5-3.5-3.5l1-1.5-2-2z" fill="#fff"/>
    </svg>
    <p>+61 03 9555 0187</p>
  </div>

  <div class="panel panel-contact">
    <svg class="icon" viewBox="0 0 28 28" aria-hidden="true">
      <circle cx="14" cy="14" r="12.5" fill="none" stroke="#fff" stroke-width="1.5"/>
      <rect x="8" y="10" width="12" height="8.5" fill="none" stroke="#fff" stroke-width="1.5"/>
      <path d="M8 10l6 5 6-5" fill="none" stroke="#fff" stroke-width="1.5"/>
    </svg>
    <p>mail@vexel-example.com.au</p>
  </div>

  <div class="panel panel-contact address">
    <svg class="icon" viewBox="0 0 28 28" aria-hidden="true">
      <circle cx="14" cy="14" r="12.5" fill="none" stroke="#fff" stroke-width="1.5"/>
      <path d="M14 21s-5-5.5-5-9a5 5 0 0 1 10 0c0 3.5-5 9-5 9z" fill="#fff"/>
      <circle cx="14" cy="12" r="1.8" fill="#5bb26d"/>
    </svg>
    <p>Vexel Consultants Pty Ltd<br>Fernhollow first floor, Tamber Street<br>Elmbrook NVA 3999 Australia</p>
  </div>
</section>

</body>
</html>
```